Kestrel Ridge Partners LLC
Business card and stationary set for Investment Firm - Financial Services
Business card and stationary set for Investment Firm
Simple
Owen Talcott
President / Founder
4820 Birchwood Lane Sparta, IL 62286
owen@talcottwealth.example
www.talcottwealth.example
jdalvin jdalvin
Also, please keep a simple, prestigious / exclusive look to the design.
Designers- I am looking for a design that uses watermarks and different parts of the logo separated out to create some originality. I only want to see the the "Professional Investment Management" one time in the design with the logo. Also, there are 2 formats of the logo in the files I uploaded. One has the graphic on the side and the other on the top. I'd like to see the use of both of these. I do like the blue on the back of the card...maybe a watermark included. The most creative will probably get the win on this. Thank you.
bluequill bluequill
Can u do some sort of star rating, which help us to make these changes,and then i will submit you stationary package with your requirements.. thanks
Also, thank you cards.
Designers - A few things I'll need in the design will be the removal of "Professional Investment Management" from the logo on the front of the card. I still like it to be on the back OR on the larger logo. I only wanted it listed on one of the logos as opposed to both of them. Also, I do like the look and feel of an exclusive, simple, unique design. I do like the back side of the card to be the blue color. I like a background image of the logo as well to add texture. Finally, I need a full stationary design including letterhead, envelopes and return of all sizes (standard and 10X 13), business cards, folders and 1/4 page paper pad. Thank you.
Vandal Vandal
Star Rating please....
Also, please include simple envelope design
Be sure to include standard stationary design as well. The font does not need to be the same as the logo on all pieces.
Designers - Feel free to remove the tagline "Professional Investment Management" in parts of the stationary and business cards. It can be included but isn't necessary. Thank you.

```html
<!DOCTYPE html>
<html lang="en">
<head>
<meta charset="utf-8">
<title>Kestrel Ridge Partners LLC — Business Card</title>
<link rel="stylesheet" href="https://fonts.googleapis.com/css2?family=Cinzel:wght@400;600&family=Open+Sans:wght@400;600;700&display=swap">
<style>
  :root {
    --page: #e9e7e3;
    --teal: #1d6677;
    --teal-dark: #17596a;
    --paper: #ffffff;
    --ink: #2e6f7f;
    --muted: #6f8f97;
    --rule: #9fb8be;
  }
  * { box-sizing: border-box; margin: 0; padding: 0; }
  html, body { width: 1200px; height: 904px; overflow: hidden; }
  body {
    background: var(--page);
    font-family: "Open Sans", Arial, sans-serif;
    position: relative;
  }
  .card {
    position: absolute;
    width: 660px;
    height: 378px;
    box-shadow: 0 6px 18px rgba(0,0,0,0.18);
  }
  .card--back {
    left: 90px; top: 48px;
    background: var(--teal);
    display: flex; align-items: center; justify-content: center;
  }
  .card--front {
    left: 450px; top: 478px;
    background: var(--paper);
    color: var(--ink);
  }
  .back-mark {
    display: flex; flex-direction: column; align-items: center; gap: 12px;
  }
  .back-mark__square {
    width: 56px; height: 56px; background: var(--paper);
  }
  .back-mark__name {
    font-family: "Cinzel", serif; font-size: 15px; letter-spacing: 2px;
    color: var(--paper); font-weight: 400;
  }
  .brand {
    position: absolute; top: 56px; left: 0; right: 0;
    display: flex; flex-direction: column; align-items: center;
  }
  .brand__square {
    width: 52px; height: 52px; background: var(--teal);
  }
  .brand__name {
    margin-top: 10px;
    font-family: "Cinzel", serif; font-size: 25px; color: var(--teal);
    letter-spacing: 0.5px; font-weight: 400;
  }
  .brand__tagline {
    margin-top: 4px; font-size: 8px; letter-spacing: 2.6px;
    text-transform: uppercase; color: var(--muted);
  }
  .person {
    position: absolute; top: 200px; left: 0; right: 0;
    text-align: center; font-size: 15px;
  }
  .person__name { font-weight: 700; color: var(--teal); }
  .person__divider { color: var(--rule); margin: 0 8px; }
  .person__title { color: var(--ink); font-size: 13px; }
  .contact {
    position: absolute; right: 34px; bottom: 34px;
    text-align: right; font-size: 12.5px; color: var(--ink);
  }
  .contact__address { margin-bottom: 10px; }
  .contact__line { display: flex; align-items: center; justify-content: flex-end; gap: 6px; }
  .contact__sep { color: var(--rule); margin: 0 4px; }
  .icon { width: 13px; height: 13px; fill: var(--teal); }
</style>
</head>
<body>
  <section class="card card--back" aria-label="Card back">
    <div class="back-mark">
      <div class="back-mark__square"></div>
      <div class="back-mark__name">Kestrel Ridge Partners LLC</div>
    </div>
  </section>

  <section class="card card--front" aria-label="Card front">
    <div class="brand">
      <div class="brand__square"></div>
      <div class="brand__name">Kestrel Ridge Partners LLC</div>
      <div class="brand__tagline">Professional Investment Management</div>
    </div>

    <p class="person">
      <span class="person__name">Owen Talcott</span><span class="person__divider">|</span><span class="person__title">President / Founder</span>
    </p>

    <div class="contact">
      <p class="contact__address">4820 Birchwood Lane, Sparta, IL 62286</p>
      <p class="contact__line">
        <svg class="icon" viewBox="0 0 16 16" aria-hidden="true"><path d="M3 1h3l1.5 4-2 1.2a9 9 0 0 0 4.3 4.3L11 8.5l4 1.5v3a2 2 0 0 1-2 2A12 12 0 0 1 1 3a2 2 0 0 1 2-2z"/></svg>
        <span>(555) 014-2783</span><span class="contact__sep">|</span>
        <svg class="icon" viewBox="0 0 16 16" aria-hidden="true"><path d="M1 3h14v10H1z M1 3l7 6 7-6" fill="none" stroke="#1d6677" stroke-width="1.6"/></svg>
        <span>owen@talcottwealth.example</span><span class="contact__sep">|</span>
        <svg class="icon" viewBox="0 0 16 16" aria-hidden="true"><circle cx="8" cy="8" r="6.5" fill="none" stroke="#1d6677" stroke-width="1.4"/><path d="M1.5 8h13M8 1.5c-3 3.5-3 9.5 0 13M8 1.5c3 3.5 3 9.5 0 13" fill="none" stroke="#1d6677" stroke-width="1.2"/></svg>
        <span>www.talcottwealth.example</span>
      </p>
    </div>
  </section>
</body>
</html>
```